Healthcare Recruitment Agency Brochure

We need our current Brochure updated as its old and dated. The brochure will be for our current and potential Clients and should provide all the necessary information regarding our services, but in a well presented, easy reading format which echoes our company Brand. The company supplies Healthcare establishments with trained healthcare Staff which can be in a variety of settings.
UPDATE: Following the submission of many designs we would like to amend the information/content to be included in the brochure and have uploaded additional information. We would like an 8 page booklet with the various sections spread out so as not to look to 'wordy' page 1 Front cover, 2 About Us, 3 Our Service, 4 Our promise, 5 Our Staff, 6 Our Ethos, 7 What Our Clients Say/Testimonials, 8 Contact Us/Back page. Please if using pictures (which is welcomed) steer away from the surgical/doctor type. We mainly provide care to the Elderly within Nursing and Residential Homes and Support Environments. Thanks

Target Market(s)

Healthcare clientell

Industry/Entity Type

Healthcare

Requirements
Must have
• Pictures, animation, easy reading, informative, tie in with website theme www.silverbrooknursingteam.co.uk
Nice to have
• open to ideas
Should not have
• very long text paragraphs

```html
<!DOCTYPE html>
<html lang="en">
<head>
<meta charset="utf-8">
<title>Silverbrook Nursing – About Us, Our Staff and Our Ethos</title>
<link href="https://fonts.googleapis.com/css2?family=Oswald:wght@400;600&family=Montserrat:ital,wght@0,400;0,600;0,700;1,600&display=swap" rel="stylesheet">
<style>
  :root {
    --bg: #e9ecee;
    --page-top: #dcecec;
    --page-bottom: #f7f9fa;
    --blue: #1f5ea8;
    --teal: #2aa58f;
    --teal-soft: #bfe3dd;
    --ink: #2f3338;
    --heading-ink: #1d1f22;
  }
  * { box-sizing: border-box; margin: 0; padding: 0; }
  html, body { width: 1200px; height: 833px; overflow: hidden; background: var(--bg); }
  body { font-family: "Montserrat", sans-serif; color: var(--ink); position: relative; }

  .spread { position: absolute; left: 60px; top: 34px; width: 1080px; height: 764px; display: flex; box-shadow: 0 4px 18px rgba(0,0,0,.12); }
  .page { position: relative; width: 540px; height: 764px; overflow: hidden;
    background: linear-gradient(160deg, var(--page-top) 0%, #eef5f5 45%, var(--page-bottom) 100%);
    border-bottom: 4px solid var(--blue); }
  .page--left { box-shadow: inset -18px 0 24px -18px rgba(0,0,0,.12); }
  .page--right { box-shadow: inset 18px 0 24px -18px rgba(0,0,0,.12); }

  .section-title { position: absolute; font-family: "Oswald", sans-serif; font-style: italic; font-weight: 400;
    font-size: 30px; letter-spacing: .5px; color: var(--heading-ink); line-height: 1; }
  .section-title strong { color: var(--blue); font-weight: 600; }
  .title-rule { position: absolute; height: 1.5px; background: var(--teal); }

  .copy { position: absolute; font-size: 8.8px; line-height: 1.3; }
  .copy p + p { margin-top: 7px; }
  .hl { color: var(--blue); font-weight: 700; }
  .lead { position: absolute; color: var(--blue); font-weight: 600; font-style: italic; font-size: 11px; line-height: 1.3; }

  .checklist { position: absolute; list-style: none; font-size: 8.8px; line-height: 1.3; }
  .checklist li { position: relative; padding-left: 20px; margin-bottom: 6px; }
  .checklist li svg { position: absolute; left: 0; top: 0; width: 11px; height: 11px; }
  .checklist--rail { border-left: 1.2px solid var(--teal); padding-left: 4px; }
  .checklist--rail li svg { left: -10px; background: var(--page-bottom); border-radius: 50%; }
  .checklist--staff li { margin-bottom: 5px; }
  .checklist li.wide { width: 300px; }
  .checklist li.narrow { width: 170px; }

  .photo { position: absolute; border-radius: 50%; }
  .photo--team { left: 262px; top: 390px; width: 250px; height: 250px; border: 5px solid var(--teal);
    background: radial-gradient(circle at 50% 45%, #ffffff 0%, #e8eef4 55%, #c9d6e2 100%); }
  .photo--care { left: 245px; top: 610px; width: 130px; height: 130px; border: 5px solid var(--blue);
    background: radial-gradient(circle at 45% 60%, #e0755a 0%, #7aa55c 45%, #3f6b35 100%); }
  .photo--nurse { left: 30px; top: 145px; width: 195px; height: 195px; border: 5px solid var(--blue);
    background: radial-gradient(circle at 50% 70%, #f4f0f2 0%, #c9a08a 55%, #8a6a5a 100%); }
  .accent-dot { position: absolute; left: 360px; top: 660px; width: 55px; height: 55px; border-radius: 50%; background: var(--teal-soft); opacity: .8; }

  .ethos-subtitle { position: absolute; left: 60px; top: 528px; font-size: 11px; font-weight: 600; letter-spacing: .8px; color: var(--ink); }
  .value { position: absolute; width: 205px; border-left: 2px solid var(--teal); padding-left: 10px; }
  .value h3 { font-family: "Oswald", sans-serif; font-weight: 600; font-style: italic; color: var(--blue);
    font-size: 13px; font-variant: small-caps; letter-spacing: .4px; margin-bottom: 4px; }
  .value h3::first-letter { font-size: 17px; }
  .value p { font-size: 8.8px; line-height: 1.35; }
</style>
</head>
<body>
<svg width="0" height="0" style="position:absolute">
  <defs>
    <symbol id="tick" viewBox="0 0 12 12">
      <circle cx="6" cy="6" r="5" fill="none" stroke="#2aa58f" stroke-width="1"/>
      <path d="M3.5 6.2 L5.3 7.9 L8.6 4.4" fill="none" stroke="#2aa58f" stroke-width="1.1" stroke-linecap="round" stroke-linejoin="round"/>
    </symbol>
  </defs>
</svg>

<div class="spread">
  <section class="page page--left">
    <h1 class="section-title" style="left:48px; top:46px;">ABOUT <strong>US</strong></h1>
    <div class="title-rule" style="left:48px; top:90px; width:444px;"></div>

    <div class="copy" style="left:48px; top:102px; width:444px;">
      <p>With over <span class="hl">15 years</span> of experience <span class="hl">Silverbrook Nursing</span> specialises in reliable recruitment solutions for the healthcare sector.</p>
      <p>We are <span class="hl">REC accredited</span> so you can rest assured that we will always be working in line with current legislation and guidelines.</p>
      <p>We strive for excellence in every aspect of our service, this includes ensuring that we are always fair, honest, and supportive of our temporary staff members, which is why we are a National Living Wage Employer.</p>
    </div>

    <p class="lead" style="left:48px; top:214px; width:444px;">We know that our Clients often have a lot on their plate, which is why we pride ourselves on being extremely accommodating:</p>

    <ul class="checklist checklist--rail" style="left:60px; top:256px; width:440px;">
      <li><svg><use href="#tick"/></svg>We can visit you at a time to suit you, to discuss your requirements and our service.</li>
      <li class="wide"><svg><use href="#tick"/></svg>We will give you our client application pack including everything you need to know, to start booking staff from Silverbrook Nursing we simply need a completed client account form.</li>
      <li class="wide"><svg><use href="#tick"/></svg>We have staff available to work at the drop of a hat-we understand the need for urgency and will make it our mission to try to help you every time.</li>
      <li class="narrow"><svg><use href="#tick"/></svg>Our friendly office staff will always be at the end of the phone to deal with your requests; we never outsource to call centres.</li>
      <li class="narrow"><svg><use href="#tick"/></svg>We will never leave you waiting and always be honest and realistic in telling you whether we can help.</li>
      <li class="narrow"><svg><use href="#tick"/></svg>When you have booked a staff member you will always receive their compliance form, in a format that suits you.</li>
      <li class="narrow"><svg><use href="#tick"/></svg>You can choose how frequently and in which format we send you your staff rotas, we will be completely flexible to your needs.</li>
      <li class="narrow"><svg><use href="#tick"/></svg>We are always interested in how we could improve; we will regularly review our service and visit you when requested.</li>
      <li class="narrow"><svg><use href="#tick"/></svg>We will regularly send you monitoring forms so you can quickly and easily pass on your feedback about the staff members we are sending you.</li>
    </ul>

    <div class="photo photo--team" role="img" aria-label="Photo of a cheerful care team in white uniforms joining hands in a high five"></div>
    <div class="accent-dot"></div>
    <div class="photo photo--care" role="img" aria-label="Photo of a smiling carer with an elderly lady in a wheelchair outdoors in a garden"></div>
  </section>

  <section class="page page--right">
    <h1 class="section-title" style="left:48px; top:46px;">OUR <strong>STAFF</strong></h1>
    <div class="title-rule" style="left:48px; top:90px; width:444px;"></div>

    <p class="copy" style="left:48px; top:100px; width:444px;">All our candidates go through a thorough vetting and recruitment process and only ever commence assignments after the following:</p>

    <div class="photo photo--nurse" role="img" aria-label="Portrait photo of a smiling care worker in a white uniform tunic"></div>

    <ul class="checklist checklist--staff" style="left:240px; top:136px; width:270px;">
      <li><svg><use href="#tick"/></svg>A face-to-face interview and skills assessment has been undertaken</li>
      <li><svg><use href="#tick"/></svg>Full employment history has been submitted</li>
      <li><svg><use href="#tick"/></svg>Right to work has been recorded and verified</li>
      <li><svg><use href="#tick"/></svg>Fitness to work has been declared</li>
      <li><svg><use href="#tick"/></svg>Two work related references have been obtained and verified</li>
      <li><svg><use href="#tick"/></svg>An enhanced DBS Certificate has been provided</li>
      <li><svg><use href="#tick"/></svg>In date, sufficient training certificates have been provided and verified or in house training courses have been attended and certificates have been issued.</li>
      <li><svg><use href="#tick"/></svg>Registration with the appropriate bodies has been verified for Registered Nurses.</li>
      <li><svg><use href="#tick"/></svg>A shadow shift has been completed if it is a brand new staff member</li>
      <li><svg><use href="#tick"/></svg>An ID Badge, uniform, and timesheets have been issued</li>
    </ul>

    <div class="copy" style="left:48px; top:402px; width:444px;">
      <p>We understand that it is imperative for our clients to only have extremely competent, fully trained staff supporting their existing team. We are proud to cover the standards set with in the <span class="hl">Care Certificate</span> in the training modules that we deliver to our staff.</p>
      <p>All training is refreshed on an annual basis and we ensure that up to date certificates are held by all staff at all times.</p>
    </div>

    <h1 class="section-title" style="left:48px; top:490px;">OUR <strong>ETHOS</strong></h1>
    <p class="ethos-subtitle">Silverbrook Nursing Team Ltd</p>
    <div class="title-rule" style="left:60px; top:546px; width:432px;"></div>

    <div class="value" style="left:48px; top:562px;">
      <h3>Honesty and Integrity.</h3>
      <p>We pride ourselves on being direct and straightforward in all our communication with our clients and potential candidates.</p>
    </div>
    <div class="value" style="left:48px; top:652px;">
      <h3>Service Excellence.</h3>
      <p>We aim to always deliver superior services to help both employers and candidates achieve their goals.</p>
    </div>
    <div class="value" style="left:285px; top:562px;">
      <h3>Dedication.</h3>
      <p>Our consultants aim to fully understand the requirements of our clients and candidates in order to find mutually beneficial solutions.</p>
    </div>
    <div class="value" style="left:285px; top:652px;">
      <h3>Leadership.</h3>
      <p>Our purpose is to become leaders in the healthcare recruitment sector, raising the bar for the entire industry.</p>
    </div>
  </section>
</div>
</body>
</html>
```